Broschüre Premium Kunstrasen
Der gesamte Auftrag wurde perfekt von Carola begleitet und abgewickelt. Prima Zusammenarbeit - ohne Wenn und Aber. Alles wurde zügig bearbeitet, sodass unsere 16-Seiten Broschüre innerhalb kurzer Zeit fertiggestellt war. Wir sind 100% zufrieden!!
Zielgruppe
Hauptsächlich (70% unserer Tätigkeit) verlegen wir Premium Kunstrasen in Gärten von Privatleuten. Schlüsselfertig .
Unsere Auftraggeber in diesem Bereich sind in der Regel zwischen 40 bis 70 Jahre alt und gut situiert.
30% unserer Tätigkeit besteht aus der reinen Lieferung von hochwertigen Kunstrasen für den Balkon, Terrasse.
Unsere Produkte haben lange Garantiezeiten von 15 Jahren. Deshalb nennen wir unsere Produkte auch Halmvollio
Aufgabenstellung
Die Broschüre wird beim Versand einer Musterbox mitgeschickt und soll ein Format von 210x210 haben.
In der Broschüre werden mehrere Produkte mit ihren technischen Eigenschaften und dem Preis abgebildet.
Die Produkte sollen in eine Story von Bildern und Texten eingebettet sein.
Die Broschüre soll aus ca. 12-16 Seiten bestehen. Dabei sollen die Texte unserer alten Broschüre übernommen werden, ebenso wie die Texte aus der Datei text 1 broschüre 2023. Wir können uns vorstellen das unsere Kunstrasensorten und die dazugehörige Beschreibung im Zusammenhang mit den ausgeführten Projekten stehen (sh. Beispiel velum sod.at). Die Fotos zu den Projekten werden wir noch uploaden.

```html
<!DOCTYPE html>
<html lang="de">
<head>
<meta charset="utf-8">
<title>Broschüre Premium Kunstrasen – Solvara</title>
<link href="https://fonts.googleapis.com/css2?family=Nunito+Sans:wght@300;400;700;800;900&display=swap" rel="stylesheet">
<style>
  :root {
    --forest: #4e6a49;
    --forest-dark: #3d5e37;
    --paper: #ffffff;
    --label: #9db297;
    --ink: #4a4a4a;
    --ink-soft: #555555;
    --badge: #cfd5cd;
    --dot-1: #3f6a39;
    --dot-2: #6aaa55;
    --dot-3: #9a9e3a;
    --dot-4: #a89b6c;
    --icon: #b9c7b6;
  }
  * { margin: 0; padding: 0; box-sizing: border-box; }
  html, body { width: 1200px; height: 600px; overflow: hidden; }
  body { font-family: "Nunito Sans", sans-serif; position: relative; background: var(--paper); }

  .page { position: absolute; top: 0; height: 600px; width: 600px; }
  .page--letter { left: 0; background: var(--forest); color: var(--paper); }
  .page--product { left: 600px; background: var(--paper); }

  .portrait-frame { position: absolute; left: 30px; top: 29px; width: 234px; height: 293px; background: var(--paper); padding: 7px; }
  .portrait { width: 100%; height: 100%; background: linear-gradient(160deg, #5d8a44 0%, #3c5a2e 45%, #1e2a3c 100%); }

  .founder { position: absolute; left: 30px; top: 338px; font-size: 12.5px; line-height: 15px; }
  .founder__name { font-weight: 700; }
  .founder__role { font-weight: 300; }

  .letter { position: absolute; left: 293px; top: 29px; width: 278px; font-size: 12px; line-height: 14.5px; font-weight: 300; text-align: justify; hyphens: manual; }
  .letter__greeting { font-weight: 700; margin-bottom: 14px; }
  .letter p { margin-bottom: 14.5px; }

  .hero-photo { position: absolute; left: 0; top: 0; width: 600px; height: 197px; background: linear-gradient(180deg, #4f7a34 0%, #6b5036 45%, #7fa54a 75%, #9fb267 100%); }

  .guarantee-badge { position: absolute; left: 505px; top: 220px; width: 62px; height: 62px; border-radius: 50%; border: 3px solid var(--badge); background: #f3f5f2; }

  .specs { position: absolute; left: 29px; top: 240px; width: 190px; color: var(--ink); font-size: 12px; }
  .spec__label { color: var(--label); font-weight: 700; font-size: 12.5px; line-height: 15px; }
  .spec__value { font-weight: 400; line-height: 15px; }
  .swatches { display: flex; gap: 6px; margin-top: 10px; }
  .swatch { width: 22px; height: 22px; border-radius: 50%; }
  .spec--use { margin-top: 24px; }
  .use-list { list-style: none; line-height: 14.5px; font-size: 12px; }
  .use-list li::before { content: "• "; }
  .spec--pile { margin-top: 17px; }
  .spec__row { display: flex; align-items: center; gap: 8px; margin-top: 3px; }
  .spec--weight { margin-top: 12px; }
  .spec--price { margin-top: 12px; }
  .price { font-size: 12.5px; }
  .price small { font-size: 8.5px; }

  .product-head { position: absolute; left: 214px; top: 263px; padding-left: 22px; border-left: 8px solid var(--forest-dark); height: 60px; color: var(--forest-dark); }
  .product-head__name { font-size: 35px; font-weight: 900; line-height: 36px; letter-spacing: 0.5px; margin-top: -3px; }
  .product-head__claim { font-size: 17.5px; font-weight: 900; line-height: 20px; margin-top: 7px; letter-spacing: 0.2px; }

  .product-text { position: absolute; left: 216px; top: 343px; width: 339px; color: var(--ink-soft); font-size: 12px; line-height: 14.5px; font-weight: 400; text-align: justify; }
  .product-text p { margin-bottom: 14.5px; }

  .turf-roll { position: absolute; left: 215px; top: 492px; width: 280px; height: 80px; background: linear-gradient(100deg, #4fa025 0%, #6cc43a 55%, #3a3d34 88%, #2a2c27 100%); clip-path: polygon(7% 40%, 88% 25%, 100% 5%, 100% 85%, 2% 100%); }
</style>
</head>
<body>
  <section class="page page--letter">
    <div class="portrait-frame">
      <div class="portrait" role="img" aria-label="Porträtfoto des Gründers vor grünem Laub"></div>
    </div>
    <div class="founder">
      <div class="founder__name">Jochen Albrecht</div>
      <div class="founder__role">Gründer &amp; Geschäftsführer</div>
    </div>
    <div class="letter">
      <div class="letter__greeting">Guten Tag lieber Kunstrasen-Interessent,</div>
      <p>vielen Dank für Ihre Anfrage nach unseren exklusiven Kunstrasen. In Ihrer Musterbox finden Sie die indiv&shy;iduell für Ihren Bedarf zusammengestellten Sorten</p>
      <p>Ganz gleich, ob Sie Ihren Garten in eine wunder&shy;bar grüne Oase verwandeln möchten oder Ihre Bodenbeläge auf Balkon und Terasse unansehn&shy;lich geworden sind: Mit unseren hochwertigen und pflegeleichten Prestige Kunstrasen zaubern Sie sich in kurzer Zeit Ihr persönliches Paradies.</p>
      <p>Unsere neue Kollektion umfasst ausschließlich au&shy;thentisch aussehende Kunstrasen, um die man Sie beneiden wird. Dabei sind unsere Sorten lichtecht und strapazierfähig. Ausgestattet mit 15 Jahren Ga&shy;rantie werden Sie auch nach vielen Jahren keinen Qualitätsunterschied sehen.</p>
      <p>Übrigens: Unsere robusten Sorten sind speichel- und leckfest und frei von bedenklichen Schadstoffen wie z.B. Blei- oder Cadium. So können auch Kinder und Tiere jederzeit bedenkenlos auf unseren Kunstrasen herumtollen.</p>
      <p>Vertrauen Sie unseren hochwertigen Sorten – so ha&shy;ben Sie lange Freude an Ihrem Einkauf!</p>
      <p>Ich freue mich von Ihnen zu hören und verbleibe zwischenzeitlich mit grünen Grüßen,</p>
    </div>
  </section>

  <section class="page page--product">
    <div class="hero-photo" role="img" aria-label="Garten mit Kunstrasen, Fasssauna, Holzstelen und Kiesweg"></div>
    <div class="guarantee-badge" role="img" aria-label="Garantie-Siegel"></div>

    <div class="specs">
      <div class="spec spec--colour">
        <div class="spec__label">Farbe</div>
        <div class="spec__value">Sommergrün</div>
        <div class="swatches">
          <span class="swatch" style="background:var(--dot-1)"></span>
          <span class="swatch" style="background:var(--dot-2)"></span>
          <span class="swatch" style="background:var(--dot-3)"></span>
          <span class="swatch" style="background:var(--dot-4)"></span>
        </div>
      </div>
      <div class="spec spec--use">
        <div class="spec__label">Geeignet für</div>
        <ul class="use-list">
          <li>Gärten</li>
          <li>Balkone und Dachterassen</li>
          <li>Innenräume</li>
          <li>Öffentliche Anlagen</li>
        </ul>
      </div>
      <div class="spec spec--pile">
        <div class="spec__label">Florhöhe</div>
        <div class="spec__row">
          <svg width="34" height="36" viewBox="0 0 34 36" aria-hidden="true">
            <line x1="2" y1="1" x2="2" y2="35" stroke="var(--icon)" stroke-width="1"/>
            <path d="M0 4 L2 1 L4 4 M0 32 L2 35 L4 32" fill="none" stroke="var(--icon)" stroke-width="1"/>
            <rect x="7" y="14" width="26" height="22" rx="3" fill="var(--icon)"/>
          </svg>
          <span class="spec__value">52mm</span>
        </div>
      </div>
      <div class="spec spec--weight">
        <div class="spec__label">Gewicht</div>
        <div class="spec__row">
          <svg width="34" height="34" viewBox="0 0 34 34" aria-hidden="true">
            <path d="M11 12 V8 a6 6 0 0 1 12 0 V12" fill="none" stroke="var(--icon)" stroke-width="3"/>
            <circle cx="17" cy="22" r="12" fill="var(--icon)"/>
          </svg>
          <span class="spec__value">3.415 gr/m²</span>
        </div>
      </div>
      <div class="spec spec--price">
        <div class="spec__label">Preis</div>
        <div class="spec__value price">35,50 € <small>zzgl. 19% MwSt</small></div>
      </div>
    </div>

    <header class="product-head">
      <h1 class="product-head__name">SOLVARA</h1>
      <h2 class="product-head__claim">LAUFEN WIE AUF WOLKEN</h2>
    </header>

    <div class="product-text">
      <p>Unser Premium Kunstrasen “Solvara” besticht durch seine Florhöhe und ist mit einem schönen Laufgefühl ausgestattet. Typischer Einsatzbereich ist der Garten. Mit seiner besonder&shy;en Halmstruktur ist diese Sorte eine wunderbare Alternative zu natürlichem Rasen.</p>
      <p>Mit der neuen Faserstruktur erwerben Sie einen wunderschönen Rasen mit sehr edler Anmutung “Solvara” ist eine der Lieb&shy;linge unserer Architekten und Garten- und Landschaftsbauer.</p>
    </div>

    <div class="turf-roll" role="img" aria-label="Aufgerollte Kunstrasenbahn"></div>
  </section>
</body>
</html>
```